Business Card design for construction company

I would like a business card design for a construction company - Harlow Constructions. I have attached the ai logo file for use. I would like the card to be very smart and clean and incorporate only white and the two colours in the logo. I would like the card to have two sides. One side can just have the logo, the other with the relevant information.

Target Market(s)

Building and Construction Clients

Industry/Entity Type

Business

Contact Information for Business Card

Name: Tom Pardoe
Company: Harlow Constructions Pty Limited
Address: 14 Mallee Crescent Carrow Vale 2093
Phone: 0427 531 068
Email: tomp@harlowbuild-example.com.au

Font styles to use
Serif
Sans Serif

Requirements
Must have
• Details noted above
• Logo as provided
• Colours as in logo
• Square edges
• A font that compliments the logo
Should not have
• Any colour other than white and those in logo
• Rounded edges

```html
<!DOCTYPE html>
<html lang="en">
<head>
<meta charset="utf-8">
<title>Harlow Constructions – Business Card</title>
<link rel="stylesheet" href="https://fonts.googleapis.com/css2?family=Michroma&family=Roboto:wght@400;500&display=swap">
<style>
  :root {
    --backdrop: #b9b9b9;
    --card: #f3f3f3;
    --blue: #1b80c8;
    --charcoal: #3b3a3c;
    --ink: #3f3f41;
    --muted: #555557;
  }
  * { box-sizing: border-box; margin: 0; padding: 0; }
  html, body { width: 1200px; height: 576px; overflow: hidden; }
  body {
    position: relative;
    background: var(--backdrop);
    font-family: "Roboto", Arial, sans-serif;
    color: var(--ink);
  }
  .card {
    position: absolute;
    top: 138px;
    width: 484px;
    height: 293px;
    background: var(--card);
  }
  .card--front { left: 81px; }
  .card--back { left: 602px; }

  /* Front */
  .wordmark {
    color: var(--charcoal);
    font-family: "Roboto", Arial, sans-serif;
    font-weight: 400;
    text-transform: uppercase;
  }
  .card--front .wordmark {
    position: absolute;
    top: 128px;
    left: 0;
    width: 100%;
    text-align: center;
    font-size: 27px;
    letter-spacing: 3px;
  }
  .site-line {
    position: absolute;
    top: 262px;
    left: 0;
    width: 100%;
    display: flex;
    justify-content: center;
    align-items: center;
    gap: 14px;
    font-size: 12.5px;
    color: var(--ink);
  }
  .site-line .rule {
    width: 66px;
    height: 2px;
    background: var(--blue);
  }

  /* Back */
  .holder {
    position: absolute;
    left: 27px;
    top: 40px;
  }
  .holder__name {
    font-family: "Michroma", Arial, sans-serif;
    font-size: 18px;
    color: var(--blue);
    letter-spacing: 0.5px;
    text-transform: uppercase;
  }
  .holder__role {
    margin-top: 6px;
    font-size: 12px;
    color: var(--muted);
  }
  .card--back .wordmark {
    position: absolute;
    right: 30px;
    top: 42px;
    width: 190px;
    text-align: center;
    line-height: 1.15;
  }
  .wordmark__main { display: block; font-size: 30px; letter-spacing: 3px; }
  .wordmark__sub { display: block; font-size: 14.5px; letter-spacing: 1.5px; margin-top: 8px; }

  .details {
    position: absolute;
    left: 27px;
    top: 171px;
    font-size: 12.5px;
  }
  .details__company {
    color: var(--blue);
    font-size: 13px;
    margin-bottom: 7px;
  }
  .details__row {
    display: flex;
    align-items: center;
    gap: 8px;
    height: 18px;
  }
  .details__row svg { width: 11px; height: 11px; flex: none; }
  .details__address { margin-top: 6px; }
</style>
</head>
<body>
  <section class="card card--front">
    <div class="wordmark">Harlow Constructions</div>
    <div class="site-line">
      <span class="rule"></span>
      <span>www.harlowbuild-example.com.au</span>
      <span class="rule"></span>
    </div>
  </section>

  <section class="card card--back">
    <div class="holder">
      <div class="holder__name">Tom Pardoe</div>
      <div class="holder__role">Managing Director</div>
    </div>

    <div class="wordmark">
      <span class="wordmark__main">Harlow</span>
      <span class="wordmark__sub">Constructions</span>
    </div>

    <div class="details">
      <div class="details__company">Harlow Constructions Pty Limited</div>
      <div class="details__row">
        <svg viewBox="0 0 12 12" aria-hidden="true"><path fill="#1b80c8" d="M1 4.5C1 2.5 3.5 1.5 6 1.5s5 1 5 3L9 5V4H3v1L1 4.5zM2.5 10.5 3.5 6h5l1 4.5z"/><circle cx="6" cy="8" r="1.1" fill="#f3f3f3"/></svg>
        <span>0427 531 068</span>
      </div>
      <div class="details__row">
        <svg viewBox="0 0 12 12" aria-hidden="true"><rect x="0.5" y="2" width="11" height="8" fill="#1b80c8"/><path d="M0.8 2.4 6 6.6l5.2-4.2" fill="none" stroke="#f3f3f3" stroke-width="1"/></svg>
        <span>tomp@harlowbuild-example.com.au</span>
      </div>
      <div class="details__row">
        <svg viewBox="0 0 12 12" aria-hidden="true"><g fill="none" stroke="#1b80c8" stroke-width="1.1"><circle cx="6" cy="6" r="5"/><ellipse cx="6" cy="6" rx="2.2" ry="5"/><path d="M1 6h10M2 3.5h8M2 8.5h8"/></g></svg>
        <span>www.harlowbuild-example.com.au</span>
      </div>
      <div class="details__address">14 Mallee Crescent Carrow Vale 2093</div>
    </div>
  </section>
</body>
</html>
```